Brochure for solar, battery back up and generators

I want to create some brochure type print media, it can be something we print in house.

I want it to show options with some detail for various products from Brivano to Kendro Stackcell.

What I am imagining is a few graphical depictions, of the final product, some detail in capability and some blanks for load calcs, very simple not a real load calc, and a place for a price.

```html
<!DOCTYPE html>
<html lang="en">
<head>
<meta charset="utf-8">
<title>Brightfield Sun — Energy Solutions</title>
<link href="https://fonts.googleapis.com/css2?family=Oswald:wght@500&family=Open+Sans:wght@400;600&display=swap" rel="stylesheet">
<style>
  :root{
    --green:#5ae634;
    --green-text:#3fd12a;
    --orange:#f7941d;
    --red:#f4511e;
    --red-text:#f2331c;
    --ink:#2a2a2a;
    --paper:#ffffff;
  }
  *{box-sizing:border-box;margin:0;padding:0}
  html,body{width:1200px;height:881px;overflow:hidden;background:var(--paper)}
  body{font-family:"Open Sans",Arial,sans-serif;color:var(--ink);position:relative}

  .masthead{position:absolute;left:0;top:0;width:1200px;height:67px}
  .masthead-title{position:absolute;left:52px;top:12px;font-family:"Oswald",Impact,sans-serif;font-weight:500;font-size:33px;line-height:1.1;color:var(--orange);letter-spacing:.2px}
  .service-icons{position:absolute;left:866px;top:18px;display:flex;gap:10px}
  .service-icons svg{width:37px;height:37px;fill:none;stroke:var(--orange);stroke-width:3;stroke-linecap:round;stroke-linejoin:round}

  .row{position:absolute;left:0;width:1200px;display:grid;grid-template-columns:400px 400px 400px}
  .row-top{top:67px;height:399px}
  .row-bottom{top:466px;height:415px}

  .service{display:flex;flex-direction:column}
  .service-band{height:29px;display:flex;align-items:center;justify-content:center;font-family:"Oswald",Impact,sans-serif;font-weight:500;font-size:18px;color:#fff;letter-spacing:.2px}
  .band-green{background:var(--green)}
  .band-orange{background:var(--orange)}
  .band-red{background:var(--red)}

  .service-body{padding:10px 16px 0 16px;font-size:10.2px;line-height:13.3px;text-align:justify}
  .photo{float:left;width:152px;height:152px;border-radius:15px;border:4px solid;margin:0 8px 4px 0}
  .photo-green{border-color:var(--green)}
  .photo-orange{border-color:var(--orange)}
  .photo-red{border-color:var(--red)}
  .sub-heading{clear:both;font-weight:600;font-size:15px;line-height:1.2;margin:9px 0 5px;color:#1d1d1d;text-align:left}
  .text-green{color:var(--green-text)}
  .text-orange{color:var(--orange)}
  .text-red{color:var(--red-text)}

  .spec-line{display:flex;align-items:baseline;gap:8px;margin-top:3px;font-size:9.6px;line-height:12px;color:#1d1d1d;text-align:left;white-space:nowrap}
  .spec-name{font-weight:600}
  .spec-blank{display:inline-block;width:44px;border-bottom:1px solid #1d1d1d;margin-left:2px}
  .spec-blank.wide{width:52px}

  .contact-note{margin-top:8px;border-top:3px solid var(--green);padding-top:6px;font-size:11.6px;line-height:14.5px;color:#1d1d1d;text-align:left}
</style>
</head>
<body>

<header class="masthead">
  <h1 class="masthead-title">Explore Our Revolutionary Approach to Energy Solutions</h1>
  <div class="service-icons" aria-hidden="true">
    <svg viewBox="0 0 36 36"><path d="M6 14l12-7 12 7-12 7z"/><path d="M6 14v10l12 7 12-7V14"/><path d="M18 21v10"/></svg>
    <svg viewBox="0 0 36 36"><rect x="10" y="7" width="16" height="25" rx="2"/><path d="M15 4h6"/><path d="M19 12l-4 7h5l-3 7"/></svg>
    <svg viewBox="0 0 36 36"><circle cx="18" cy="18" r="5"/><path d="M18 6v4M18 26v4M6 18h4M26 18h4M9.5 9.5l3 3M23.5 23.5l3 3M9.5 26.5l3-3M23.5 12.5l3-3"/></svg>
    <svg viewBox="0 0 36 36"><path d="M5 22l3-9h20l3 9v6H5z"/><circle cx="11" cy="24" r="2"/><circle cx="25" cy="24" r="2"/><path d="M8 28v3M28 28v3"/></svg>
    <svg viewBox="0 0 36 36"><rect x="7" y="6" width="14" height="25" rx="2"/><path d="M4 31h20M21 13h4l3 4v9a2 2 0 0 0 4 0V12"/><path d="M15 11l-3 6h4l-2 6"/></svg>
    <svg viewBox="0 0 36 36"><circle cx="17" cy="18" r="12"/><path d="M13 14v4M21 14v4"/><path d="M14 23h6"/><path d="M28 20l-4 7h5l-3 6"/></svg>
  </div>
</header>

<section class="row row-top">
  <article class="service">
    <h2 class="service-band band-green">Creating a Cleaner World With Solar Power Solutions</h2>
    <div class="service-body">
      <div class="photo photo-green" role="img" aria-label="Installers fitting solar panels on a rooftop beside green fields" style="background:linear-gradient(160deg,#6aa84f 0%,#7fa7d6 45%,#2f5fa8 100%)"></div>
      <p>Not only is it our goal to provide you with a solar power system you can rely on, but we’re also changing the world while we’re at it. We are at the forefront of the movement to create a sustainable future for our society. No job is too small or too large for our team of experienced contractors. Every solar panel installation job we complete at Brightfield Sun reduces our collective environmental impact and protects our future. If you’re ready to receive design, installation, and maintenance services from a team of solar power system experts, you’ve come to the right place. We guarantee exceptional customer service and can’t wait to get started.</p>
      <h3 class="sub-heading">Small Investment with Worldwide Benefits</h3>
      <p class="text-green">We believe that solar power is the ideal energy alternative from both an environmental and financial standpoint. With our solar panel systems, you can save money in the long run and feel good about going green. We will discuss your energy objectives and solar options during your initial site assessment to ensure you are completely satisfied with every aspect of your new system. Our knowledgeable team will guarantee that you are able to maximize your investment, minimize your cost, and increase your overall property value. Give us a call today to receive a free estimate.</p>
      <div class="spec-line"><span class="spec-name text-green">Solar Array</span><span>Daily load:<span class="spec-blank"></span> kWh</span><span>System:<span class="spec-blank"></span> kW</span><span>Price: $<span class="spec-blank wide"></span></span></div>
    </div>
  </article>

  <article class="service">
    <h2 class="service-band band-orange">Solar-Powered Generators You Can Rely On</h2>
    <div class="service-body">
      <div class="photo photo-orange" role="img" aria-label="Brivano portable solar generator unit with its lid open" style="background:linear-gradient(160deg,#9aa3a8 0%,#e4e7e8 55%,#c9cdcf 100%)"></div>
      <p>In the event of a power outage, you shouldn’t have to scramble to find a source of light and heat. You deserve to feel prepared with a back-up energy source that you and your family can always depend on. Brivano solar generators from Brightfield Sun are the ideal solution for your on-demand power needs. You can achieve the security and peace of mind of a multi-fuel generator while protecting the environment. All homeowners should consider using a clean energy alternative for their generator needs. Whether you are looking for a solution for occasional on-demand power or need a short-term emergency solution, we have you covered.</p>
      <h3 class="sub-heading">Discover Your Long-Lasting Clean Energy Source</h3>
      <p class="text-orange">Though slightly pricier up front, Brivano solar-powered generators are a great option to consider for a long-term investment. They last for several decades, operate silently, and don’t release any harmful emissions. With simple maintenance and no oil or air filter changes required, you’ll also save time and money in the long run. Our team of experts will handle the installation and maintenance of your solar-powered generator. With our professional recommendations, you’ll be prepared with the perfect amount of power for your family’s unique needs. Give us a call today for a free quote.</p>
      <div class="spec-line"><span class="spec-name text-orange">Brivano</span><span>Running load:<span class="spec-blank"></span> W</span><span>Hours:<span class="spec-blank"></span></span><span>Price: $<span class="spec-blank wide"></span></span></div>
    </div>
  </article>

  <article class="service">
    <h2 class="service-band band-red">We Install Commercial EV Charging Stations</h2>
    <div class="service-body">
      <div class="photo photo-red" role="img" aria-label="Driver plugging an electric car into a public charging station at sunset" style="background:linear-gradient(160deg,#3c6fb6 0%,#e88a3a 55%,#2b2b3a 100%)"></div>
      <p>As electric vehicles (EVs) become increasingly more commonplace, the need for convenient charging options is more pressing than ever. Drivers of these environmentally friendly cars depend on EV charging stations located either at their homes or throughout the city to operate their vehicle throughout the day. By adding one of these charging stations to your commercial building or multi-family property, you can provide a much-needed service to your employees, customers, and residents. If you are interested in learning more about how to integrate our services into your business, give us a call today. Our team of experts would be happy to answer any questions you may have.</p>
      <h3 class="sub-heading">Call Us for Professional EV Charger Installation</h3>
      <p class="text-red">We’re on the road to creating a more EV-friendly society by building a more convenient charging infrastructure throughout the country. If you’re ready to join the movement and stay ahead of the game, we’re ready to help you achieve your goals. You can help your business meet the ever-growing demand for electric charging stations with our commercial charging stations. Our high-power chargers are professionally-installed and maintained by our EV experts. We are dedicated to providing the excellent customer service and top-quality products you deserve. Reach out to us today to receive your free estimate.</p>
    </div>
  </article>
</section>

<section class="row row-bottom">
  <article class="service">
    <h2 class="service-band band-red">Ease Your Worries With Our Solar Battery Back-Ups</h2>
    <div class="service-body">
      <div class="photo photo-red" role="img" aria-label="House roof covered with solar panels under a blue sky" style="background:linear-gradient(160deg,#8fc3ec 0%,#2c63c4 50%,#6b6f74 100%)"></div>
      <p>Nothing makes you feel quite as helpless as being stuck without power during a massive power outage. Loss of power is not only a frustrating hindrance to your daily routine, but it can also become a health risk to you and your loved ones. In order to avoid long-term exposure to the summer heat or winter cold, you should consider installing a battery backup ahead of time. Our Kendro Stackcell back-ups give you peace of mind that you will always have a source of power to rely on during uncertain times. You can stay ahead of the next power grid shutdown with a battery backup from the experts at Brightfield Sun.</p>
      <h3 class="sub-heading">Explore the Benefits of Clean Alternatives</h3>
      <p class="text-red">Whether or not your primary source of power is derived from a solar panel system, solar battery backups are a great option to consider as an addition to your home. In addition to providing support during power outages, our battery backups offer an impressive return on investment. You can avoid peak utility rates by drawing power from this pre-charged source during the more expensive times of day. You can also store solar electricity throughout the day for nighttime use. If you’re ready to reduce your overall utility bills and experience peace of mind during emergencies, give us a call today. Our experts provide professional installation and maintenance.</p>
      <div class="spec-line"><span class="spec-name text-red">Kendro Stackcell</span><span>Backup load:<span class="spec-blank"></span> kWh</span><span>Units:<span class="spec-blank" style="width:26px"></span></span><span>Price: $<span class="spec-blank"></span></span></div>
    </div>
  </article>

  <article class="service">
    <h2 class="service-band band-green">We Install Residential Electric Vehicle Chargers</h2>
    <div class="service-body">
      <div class="photo photo-green" role="img" aria-label="Row of wall-mounted home battery and charger units" style="background:linear-gradient(160deg,#bfe6ec 0%,#7fc9d6 50%,#d9eef1 100%)"></div>
      <p>Electric vehicles (EVs) are the everyday transportation method of the future. As a driver of an EV, you are a part of a movement to lower emissions and protect our planet. You deserve a convenient way to charge at home instead of constantly searching for public charging stations throughout your city. Whether you are looking to install a new EV charger in your home or upgrade your existing charger, our contractors have you covered. We will ensure you are connected with the best charger for you and your family’s unique needs. Give us a call today for a free estimate.</p>
      <h3 class="sub-heading">Choose the Road to a Cleaner Future</h3>
      <p class="text-green">The ever-growing network of charging stations throughout the country is making the EV driving experience more convenient than ever. However, no public charging station beats the ability to refuel right out of your personal garage. Our efficient home charging stations are the game-changing level of convenience you’ve been looking for. Soon enough, you’ll be able to plug your vehicle in after work and rest easy knowing it will be fully charged by the morning. Sit back, relax, and let our team of technicians handle the installation process from start to finish. If you’re ready to transform your EV charging experience, give us a call today for a free estimate.</p>
      <div class="spec-line"><span class="spec-name text-green">Home Charger</span><span>Circuit:<span class="spec-blank"></span> A</span><span>Daily miles:<span class="spec-blank"></span></span><span>Price: $<span class="spec-blank wide"></span></span></div>
    </div>
  </article>

  <article class="service">
    <h2 class="service-band band-orange">Electrical Contractors You Can Depend On</h2>
    <div class="service-body">
      <div class="photo photo-orange" role="img" aria-label="Electrician in a hard hat testing a panel with a multimeter" style="background:linear-gradient(160deg,#f2d23c 0%,#c9c9c4 50%,#5d6166 100%)"></div>
      <p>When searching for a contractor to handle your next electrical project, you shouldn’t trust just anyone. To get the job done right, you need an electrician on your side who is reliable, efficient, and has been highly-trained in the latest technologies. The team of contractors at Brightfield Sun has you covered for your electrical maintenance, repair, design, and installation needs. As a part of our mission to advance our society’s energy infrastructure, we provide professional recommendations and can handle the ins and outs of your residential and commercial electricity needs. If you’re ready to connect with a team of electrical contractors you can trust, give us a call today to get started.</p>
      <h3 class="sub-heading">Contractors Dedicated to Customer Satisfaction</h3>
      <p class="text-orange">You deserve an electrical contractor who is truly focused on your satisfaction, not sales. We work diligently to ensure that even the most complex electrical projects are completed safely and that the results exceed your expectations. If you have an installation project or an unexpected electrical issue on your plate, give us a call today. We would be happy to provide a free estimate for our services and get started as soon as possible.</p>
      <p class="contact-note">Estimate : Larkmont, CA : Brightfield SunGet an estimate of our solar power solutions and reliable construction services at Brightfield Sun in Larkmont, CA.brightfieldsun.com</p>
    </div>
  </article>
</section>

</body>
</html>
```